Clothing Brand E-Commerce Website Design

We would like you to provide an ecommerce design template in layered PSD for our clothing/fashion brand website called "TrelWick".
We want the site to have a simple but sleek design similar to the following sites:
http://www.pivorane.com/
http://corvatelle.com/
http://www.dulvenor.com/
We want it to look stunning and blow the example sites out of the water. For color scheme, please use your imagination and try to impress us with your creativity.
We like teal and beige pink, with teal dominant.
Teal #7AFFFF / #46C6C6
Beige/pink #FF7B7C / #C74646
We want you to develop the design for 3 pages:
1) Home Page
Samples:
http://www.pivorane.com/
http://corvatelle.com/
http://www.dulvenor.com/
2) Products List Page (e.g., lists all "Dresses" when category is selected)
http://www.pivorane.com/shop/casual-dresses
http://www.dulvenor.com/index.php?main_page=index&cPath=3
http://corvatelle.com/modest-dresses.html
http://www.quillmarsh.com/Product/Category.aspx?br=q47&category=dress_maxi
3) Product Detail Page (e.g., individual product page with "Add to Cart")
http://www.pivorane.com/shop/dresses/lumen-fern-dress
http://corvatelle.com/modest-dresses/modest-dress-tova.html
http://www.dulvenor.com/index.php?main_page=product_info&cPath=3&products_id=297
Industry/Entity Type
Fashion

```html
<!DOCTYPE html>
<html lang="en">
<head>
<meta charset="utf-8">
<title>TrelWick — Products</title>
<link href="https://fonts.googleapis.com/css2?family=Raleway:wght@400;500;600&display=swap" rel="stylesheet">
<style>
:root{
  --ink:#1a1a1a;
  --bar:#262626;
  --nav:#d3d3d3;
  --nav-line:#ffffff;
  --muted:#555;
  --frame:#d0d0d0;
  --price:#8b1a1a;
  --star:#f5b800;
  --star-edge:#d99400;
  --white:#fff;
}
*{box-sizing:border-box;margin:0;padding:0}
html,body{width:1200px;height:1044px;overflow:hidden;background:var(--white)}
body{position:relative;font-family:"Raleway",sans-serif;color:var(--ink)}
.abs{position:absolute}

.top-bar{left:0;top:0;width:1200px;height:32px;background:var(--bar);color:#ddd;font-size:10px}
.top-bar .promo{left:583px;top:10px}
.top-bar .phone{left:856px;top:10px}

.welcome{left:145px;top:80px;font-size:10px}
.welcome b{font-size:12px;font-weight:600}
.brand-name{left:0;width:1200px;top:55px;text-align:center;font-size:46px;font-weight:400;color:var(--ink);letter-spacing:1px}
.account-links{right:152px;top:56px;font-size:10px;color:var(--muted)}
.account-links span{margin:0 8px}

.main-nav{left:141px;top:133px;width:907px;height:20px;background:var(--nav);display:grid;grid-template-columns:108px 133px 104px 109px 123px 112px 128px 90px}
.main-nav a{font-size:12px;text-align:center;line-height:20px;color:var(--ink);text-decoration:none;border-right:1px solid var(--nav-line)}
.main-nav a:last-child{border-right:none}

.search{left:143px;top:197px;width:175px;height:25px;border:1px solid #bbb;font-size:10px;color:#888;padding:6px 14px}
.search svg{position:absolute;right:12px;top:6px}

.sidebar h3{font-size:12px;font-weight:500;position:absolute;left:145px}
.sidebar ul{list-style:none;position:absolute;left:145px;font-size:10.5px;color:#333}
.radio li{height:20px;display:flex;align-items:center;gap:6px}
.radio i{width:13px;height:13px;border-radius:50%;border:1px solid #c4c4c4;background:linear-gradient(#fff,#e6e6e6);display:inline-block;position:relative}
.radio i.on::after{content:"";position:absolute;left:3px;top:3px;width:5px;height:5px;border-radius:50%;background:#2b6fb8}
.links li{height:19.7px}

.crumb{left:368px;top:180px;font-size:10px}

.card{position:absolute;width:163px}
.card .frame{height:276px;border:3px solid var(--frame);background:var(--white);padding:4px}
.card .photo{width:100%;height:100%}
.card .title{display:flex;justify-content:space-between;align-items:baseline;margin-top:11px;font-size:14px;padding:0 3px}
.card .title em{font-style:normal;font-size:10px;color:var(--price);font-weight:600}
.card .stars{display:flex;gap:1px;margin-top:2px;padding-left:2px}

.pager{left:362px;top:908px;display:flex;gap:7px;align-items:center}
.pager span{height:23px;min-width:23px;border-radius:12px;background:linear-gradient(#fff,#d6d6d6);box-shadow:0 1px 2px rgba(0,0,0,.35);font-size:10px;display:flex;align-items:center;justify-content:center;gap:4px;padding:0 6px}
.pager span.on{background:linear-gradient(#9a9a9a,#555);color:#fff}
.pager b{width:11px;height:11px;border-radius:50%;background:#333;display:inline-block;position:relative}
.pager b::after{content:"";position:absolute;top:3px;border:2.5px solid transparent}
.pager b.l::after{left:1px;border-right:4px solid #fff}
.pager b.r::after{left:4px;border-left:4px solid #fff}

.footer{left:0;top:978px;width:1200px;height:66px;background:var(--bar);color:#eee}
.footer .legal{left:143px;top:22px;font-size:10px}
.footer .copy{right:155px;top:21px;font-size:11px;text-align:right;line-height:20px}
.footer .copy small{font-size:9px}
.tab{left:584px;top:951px}
</style>
</head>
<body>

<div class="abs top-bar">
  <span class="abs promo">Take and Extra 20% OFF Your Purchase - Code: June 14</span>
  <span class="abs phone">Call Customer Services on: +1-888-555-0142</span>
</div>

<p class="abs welcome">Welcome visitor you can <b>log in</b> or create an <b>account</b></p>
<div class="abs brand-name">TrelWick</div>
<p class="abs account-links">Order list<span>|</span>My Account<span>|</span>Checkout ( 0 )</p>

<nav class="abs main-nav">
  <a href="#">HOME</a><a href="#">WOMEN</a><a href="#">MEN</a><a href="#">PAGES</a><a href="#">CONTACT US</a><a href="#">FEATURES</a><a href="#">TYPOGRAPHY</a><a href="#">SHOP</a>
</nav>

<aside class="sidebar">
  <div class="abs search">Search . . .
    <svg width="11" height="11" viewBox="0 0 11 11"><circle cx="4.5" cy="4.5" r="3.4" fill="none" stroke="#222" stroke-width="1.6"/><line x1="7" y1="7" x2="10.3" y2="10.3" stroke="#222" stroke-width="1.8"/></svg>
  </div>
  <h3 style="top:241px">By Price:</h3>
  <ul class="radio" style="top:260px">
    <li><i></i>$14 -- $32</li><li><i></i>$32 -- $50</li><li><i></i>$50 -- $68</li><li><i class="on"></i>$68 and over</li>
  </ul>
  <h3 style="top:352px">By Size:</h3>
  <ul class="radio" style="top:373px">
    <li><i></i>Small</li><li><i></i>Medium</li><li><i></i>Large</li><li><i></i>Extra Large</li><li><i></i>Extra Large</li>
  </ul>
  <h3 style="top:487px">Shop By Style</h3>
  <ul class="links" style="top:521px">
    <li>Modern Femme</li><li>Boho</li><li>Heritage</li><li>Capsule 2.1</li><li>Minimalist</li><li>Free Spirit</li><li>Swimwear</li>
  </ul>
  <h3 style="top:692px">SPECIAL SIZES</h3>
  <ul class="links" style="top:729px">
    <li>Plus</li><li>Petite</li><li>Maternity</li><li>Extended Shoe Sizes</li><li>Juniors</li>
  </ul>
</aside>

<p class="abs crumb">Home &gt; Products</p>

<svg width="0" height="0" style="position:absolute">
  <defs>
    <symbol id="star" viewBox="0 0 20 20"><path d="M10 1.5l2.6 5.4 5.9.8-4.3 4.1 1.1 5.9L10 14.9l-5.3 2.8 1.1-5.9L1.5 7.7l5.9-.8z" fill="var(--star)" stroke="var(--star-edge)" stroke-width="1"/></symbol>
  </defs>
</svg>

<main>
  <article class="card" style="left:361px;top:208px">
    <div class="frame"><div class="photo" role="img" aria-label="Model in a turquoise dress with navy bands" style="background:linear-gradient(#fafafa 10%,#2fd0c8 40%,#21b9b5 75%,#fafafa)"></div></div>
    <div class="title">Dress # 1<em>$ 100</em></div>
    <div class="stars"><svg width="17" height="17"><use href="#star"/></svg><svg width="17" height="17"><use href="#star"/></svg><svg width="17" height="17"><use href="#star"/></svg><svg width="17" height="17"><use href="#star"/></svg><svg width="17" height="17"><use href="#star"/></svg></div>
  </article>
  <article class="card" style="left:535px;top:208px">
    <div class="frame"><div class="photo" role="img" aria-label="Model in a mint lace dress" style="background:linear-gradient(#fafafa 10%,#c6ebdc 40%,#b8e3d2 75%,#fafafa)"></div></div>
    <div class="title">Dress # 2<em>$ 100</em></div>
    <div class="stars"><svg width="17" height="17"><use href="#star"/></svg><svg width="17" height="17"><use href="#star"/></svg><svg width="17" height="17"><use href="#star"/></svg></div>
  </article>
  <article class="card" style="left:709px;top:208px">
    <div class="frame"><div class="photo" role="img" aria-label="Model in a red and navy striped dress" style="background:linear-gradient(#fafafa 10%,#c7404a 40%,#2a2f4a 75%,#fafafa)"></div></div>
    <div class="title">Dress # 3<em>$ 100</em></div>
    <div class="stars"><svg width="17" height="17"><use href="#star"/></svg><svg width="17" height="17"><use href="#star"/></svg><svg width="17" height="17"><use href="#star"/></svg><svg width="17" height="17"><use href="#star"/></svg></div>
  </article>
  <article class="card" style="left:883px;top:208px">
    <div class="frame"><div class="photo" role="img" aria-label="Model in an aqua patterned dress" style="background:linear-gradient(#fafafa 10%,#8fdcd3 40%,#7ed2c8 75%,#fafafa)"></div></div>
    <div class="title">Dress # 4<em>$ 100</em></div>
    <div class="stars"><svg width="17" height="17"><use href="#star"/></svg><svg width="17" height="17"><use href="#star"/></svg></div>
  </article>

  <article class="card" style="left:361px;top:553px">
    <div class="frame"><div class="photo" role="img" aria-label="Model in a floral print dress" style="background:linear-gradient(#fafafa 10%,#f2c6a4 40%,#ec9a7a 75%,#fafafa)"></div></div>
    <div class="title">Dress # 5<em>$ 100</em></div>
    <div class="stars"><svg width="17" height="17"><use href="#star"/></svg><svg width="17" height="17"><use href="#star"/></svg><svg width="17" height="17"><use href="#star"/></svg></div>
  </article>
  <article class="card" style="left:535px;top:553px">
    <div class="frame"><div class="photo" role="img" aria-label="Model in a navy dress with green sleeves and a straw hat" style="background:linear-gradient(#fafafa 10%,#2c9a6e 30%,#2d4a7c 60%,#fafafa)"></div></div>
    <div class="title">Dress # 6<em>$ 100</em></div>
    <div class="stars"><svg width="17" height="17"><use href="#star"/></svg></div>
  </article>
  <article class="card" style="left:709px;top:553px">
    <div class="frame"><div class="photo" role="img" aria-label="Model in a cream sweater and teal maxi skirt" style="background:linear-gradient(#fafafa 10%,#efe3d6 35%,#1f6b65 60%,#fafafa)"></div></div>
    <div class="title">Dress # 7<em>$ 100</em></div>
    <div class="stars"><svg width="17" height="17"><use href="#star"/></svg><svg width="17" height="17"><use href="#star"/></svg><svg width="17" height="17"><use href="#star"/></svg><svg width="17" height="17"><use href="#star"/></svg></div>
  </article>
  <article class="card" style="left:883px;top:553px">
    <div class="frame"><div class="photo" role="img" aria-label="Model in a pink striped cardigan and dark jeans" style="background:linear-gradient(#fafafa 10%,#f0b7bd 45%,#1f2536 80%,#fafafa)"></div></div>
    <div class="title">Dress # 7<em>$ 100</em></div>
    <div class="stars"><svg width="17" height="17"><use href="#star"/></svg><svg width="17" height="17"><use href="#star"/></svg><svg width="17" height="17"><use href="#star"/></svg><svg width="17" height="17"><use href="#star"/></svg><svg width="17" height="17"><use href="#star"/></svg></div>
  </article>
</main>

<nav class="abs pager">
  <span><b class="l"></b>First</span>
  <span><b class="l"></b></span>
  <span class="on">1</span><span>2</span><span>3</span><span>4</span>
  <span><b class="r"></b></span>
  <span>Last<b class="r"></b></span>
</nav>

<svg class="abs tab" width="32" height="28" viewBox="0 0 32 28"><path d="M16 0L32 28H0z" fill="var(--bar)"/><path d="M16 12v11M10.5 17.5h11" stroke="#fff" stroke-width="2.4"/></svg>

<footer class="abs footer">
  <p class="abs legal">Privacy &amp; Cookies Terms &amp; Conditions Accessibility Store Directory About Us</p>
  <p class="abs copy">©2014 TrelWick Shop Ltd<br><small>All rights reserved</small></p>
</footer>

</body>
</html>
```